Medical Cannabis company is looking for a LOGO design *

SILVER MERIDIAN (SM) is a new company in the Israeli medical cannabis industry. We will engage in PREMIUM medical cannabis growing and cultivation and also manufacturing of HIGH-END cannabis based medical products.
the design should reflect luxury, high-end and Pharma-grade products.
the design should use color GOLD and NOT using the famous cannabis leaf !

Target Market(s)

international medical cannabis Pharmaceutical companies
and of course local and international patients

Contact Information for Business Card

Ron Ben-Amit
Founder and CEO

Silver Meridian
Medical grade cannabis

ronbenamit@mailpost-example.com
972-52-3186407

Colors
ffc214
fbed22

Requirements
Must have
• clean and simple
• luxury
• gold !!
• (can also have green for Cannabis and/or blue for Pharma)
Should not have
• cannabis leaf

```html
<!DOCTYPE html>
<html lang="en">
<head>
<meta charset="utf-8">
<title>Silver Meridian — Business Cards</title>
<link href="https://fonts.googleapis.com/css2?family=Lato:wght@400;700&display=swap" rel="stylesheet">
<style>
  :root {
    --backdrop: #4a5566;
    --card-white: #ffffff;
    --brand-yellow: #ffc214;
    --gold-dark: #a57a45;
    --gold-mid: #c89a5c;
    --gold-light: #f6d08e;
    --mark-gold: #b38549;
    --ink: #1f1f1f;
  }
  * { box-sizing: border-box; margin: 0; padding: 0; }
  html, body { width: 1200px; height: 1000px; overflow: hidden; }
  body {
    background: var(--backdrop);
    font-family: "Lato", sans-serif;
    position: relative;
  }
  .card {
    position: absolute;
    width: 516px;
    height: 294px;
    overflow: hidden;
    background: var(--card-white);
  }
  .card--rounded { border-radius: 30px; }

  .card--front-rounded { left: 65px; top: 102px; width: 513px; height: 291px; }
  .card--front-square  { left: 622px; top: 260px; }
  .card--back-rounded  { left: 61px; top: 446px; width: 518px; }
  .card--back-square   { left: 620px; top: 601px; }

  /* Front: brand mark */
  .brand-front {
    position: absolute;
    left: 0; right: 0;
    top: 62px;
    text-align: center;
    color: var(--mark-gold);
    font-weight: 400;
  }
  .brand-front__initials {
    display: block;
    font-size: 94px;
    line-height: 1;
    letter-spacing: 2px;
  }
  .brand-front__name {
    display: block;
    margin-top: 14px;
    font-size: 25px;
    letter-spacing: 1.5px;
  }

  /* Back */
  .back-wave { position: absolute; inset: 0; width: 100%; height: 100%; }
  .holder {
    position: absolute;
    left: 28px;
    top: 84px;
    color: var(--ink);
  }
  .holder__name { font-size: 25px; font-weight: 400; line-height: 1.2; }
  .holder__title { font-size: 15px; margin-top: 6px; }

  .contact-list {
    position: absolute;
    left: 28px;
    top: 194px;
    list-style: none;
    color: var(--ink);
    font-size: 15.5px;
  }
  .contact-list__item {
    display: flex;
    align-items: center;
    height: 29px;
  }
  .contact-list__icon { width: 13px; height: 13px; margin-right: 12px; fill: var(--ink); }

  .brand-back {
    position: absolute;
    right: 22px;
    top: 124px;
    width: 190px;
    text-align: center;
    color: var(--ink);
  }
  .brand-back__initials {
    display: block;
    font-size: 72px;
    line-height: 1;
    letter-spacing: 1px;
  }
  .brand-back__name { display: block; font-size: 15.5px; margin-top: 4px; letter-spacing: 0.3px; }
  .brand-back__tagline { display: block; font-size: 14.5px; margin-top: 1px; }
</style>
</head>
<body>

  <!-- Front, rounded corners -->
  <section class="card card--rounded card--front-rounded">
    <div class="brand-front">
      <span class="brand-front__initials">SM</span>
      <span class="brand-front__name">SILVER MERIDIAN</span>
    </div>
  </section>

  <!-- Front, square corners -->
  <section class="card card--front-square">
    <div class="brand-front">
      <span class="brand-front__initials">SM</span>
      <span class="brand-front__name">SILVER MERIDIAN</span>
    </div>
  </section>

  <!-- Back, rounded corners -->
  <section class="card card--rounded card--back-rounded">
    <svg class="back-wave" viewBox="0 0 518 294" preserveAspectRatio="none" aria-hidden="true">
      <defs>
        <linearGradient id="goldSheenA" x1="0" y1="0" x2="1" y2="0">
          <stop offset="0" stop-color="#a8793f"/>
          <stop offset="0.35" stop-color="#c99c60"/>
          <stop offset="0.62" stop-color="#f8d393"/>
          <stop offset="1" stop-color="#b0854b"/>
        </linearGradient>
      </defs>
      <rect width="518" height="294" fill="var(--brand-yellow)"/>
      <path d="M0,148 C110,190 200,190 300,140 S450,70 518,82 L518,294 L0,294Z" fill="#ffffff"/>
      <path d="M0,158 C110,196 210,194 305,152 S450,98 518,112 L518,294 L0,294Z" fill="url(#goldSheenA)"/>
    </svg>
    <div class="holder">
      <p class="holder__name">Ron Ben-Amit</p>
      <p class="holder__title">Founder and CEO</p>
    </div>
    <ul class="contact-list">
      <li class="contact-list__item">
        <svg class="contact-list__icon" viewBox="0 0 16 16"><path d="M3.6 1 6 3.6 4.7 5.6c.8 1.9 2.2 3.4 4.1 4.4L10.6 8.6 15 11l-.9 3.2C13.7 15 12.8 15.2 12 15 6.3 13.5 2.3 9.4 1 3.8.8 3 1.1 2 2 1.6Z"/></svg>
        972-52-3186407
      </li>
      <li class="contact-list__item">
        <svg class="contact-list__icon" viewBox="0 0 16 16"><path d="M1 3h14v1.2L8 9 1 4.2Z M1 5.8 8 10.6 15 5.8V13H1Z"/></svg>
        ronbenamit@mailpost-example.com
      </li>
    </ul>
    <div class="brand-back">
      <span class="brand-back__initials">SM</span>
      <span class="brand-back__name">SILVER MERIDIAN</span>
      <span class="brand-back__tagline">Medical grade cannabis</span>
    </div>
  </section>

  <!-- Back, square corners -->
  <section class="card card--back-square">
    <svg class="back-wave" viewBox="0 0 516 294" preserveAspectRatio="none" aria-hidden="true">
      <defs>
        <linearGradient id="goldSheenB" x1="0" y1="0" x2="1" y2="0">
          <stop offset="0" stop-color="#a8793f"/>
          <stop offset="0.35" stop-color="#c99c60"/>
          <stop offset="0.62" stop-color="#f8d393"/>
          <stop offset="1" stop-color="#b0854b"/>
        </linearGradient>
      </defs>
      <rect width="516" height="294" fill="var(--brand-yellow)"/>
      <path d="M0,150 C110,190 200,190 300,140 S450,70 516,82 L516,294 L0,294Z" fill="#ffffff"/>
      <path d="M0,160 C110,196 210,194 305,152 S450,98 516,112 L516,294 L0,294Z" fill="url(#goldSheenB)"/>
    </svg>
    <div class="holder">
      <p class="holder__name">Ron Ben-Amit</p>
      <p class="holder__title">Founder and CEO</p>
    </div>
    <ul class="contact-list">
      <li class="contact-list__item">
        <svg class="contact-list__icon" viewBox="0 0 16 16"><path d="M3.6 1 6 3.6 4.7 5.6c.8 1.9 2.2 3.4 4.1 4.4L10.6 8.6 15 11l-.9 3.2C13.7 15 12.8 15.2 12 15 6.3 13.5 2.3 9.4 1 3.8.8 3 1.1 2 2 1.6Z"/></svg>
        972-52-3186407
      </li>
      <li class="contact-list__item">
        <svg class="contact-list__icon" viewBox="0 0 16 16"><path d="M1 3h14v1.2L8 9 1 4.2Z M1 5.8 8 10.6 15 5.8V13H1Z"/></svg>
        ronbenamit@mailpost-example.com
      </li>
    </ul>
    <div class="brand-back">
      <span class="brand-back__initials">SM</span>
      <span class="brand-back__name">SILVER MERIDIAN</span>
      <span class="brand-back__tagline">Medical grade cannabis</span>
    </div>
  </section>

</body>
</html>
```